Magician | Speaker looks for an innovative business card design

I'm a magician and public speaker offering artistic and modern magical experiences.
I'm based in Brussels (Belgium.) I love magic performed up-close, creating a space of intimacy, even when I'm on stage.
The final design should communicate professionalism, elegance, artistry, and a friendly kind personality

I would like to see designs based either on my photos and/or the way I sign my name Remy Vok (see attached files for more info.)
Additional photos and more info about what I offer can be seen at www.remy-vok.net

My current business card design is also attached. I like the fact that the reverse of my current design includes quotes from master magicians about magic, changing the way my participants see the art of magic.

Note: I would like a double-sided card design. However, I need white space on the reverse to be able to write things on for my performances.

Details to include on the card:
Artist name: Remy Vok
Offer: magician + (public) speaker or magic + (public) speaking (the + sign can be replaced by another character, like a bullet or a pipe)
Phone: +32 471 265 903
Email: book@remy-vok.net
(optional) Website: www.remy-vok.net or remy-vok.net

Target Market(s)

Corporate, organisations, companies as well as individuals

Industry/Entity Type

Artists

Colors

Designer to choose colors to be used in the design.

Requirements
Nice to have
• A side with a mirror could be nice

```html
<!DOCTYPE html>
<html lang="en">
<head>
<meta charset="utf-8">
<title>Remy Vok — Business Card</title>
<link rel="stylesheet" href="https://fonts.googleapis.com/css2?family=Mulish:wght@400;600;700&display=swap">
<style>
  :root {
    --page-bg: #ffffff;
    --card-bg: #000000;
    --text-main: #ffffff;
    --text-soft: #e6e6e6;
    --text-muted: #9a9a9a;
  }
  * { margin: 0; padding: 0; box-sizing: border-box; }
  html, body {
    width: 1200px;
    height: 1200px;
    overflow: hidden;
    background: var(--page-bg);
  }
  .canvas {
    position: relative;
    width: 1200px;
    height: 1200px;
  }
  .card-front {
    position: absolute;
    left: 76px;
    top: 326px;
    width: 1048px;
    height: 548px;
    background: var(--card-bg);
    font-family: "Mulish", sans-serif;
    color: var(--text-main);
  }
  .brand-name {
    position: absolute;
    left: 0;
    right: 0;
    top: 170px;
    text-align: center;
    font-size: 112px;
    font-weight: 700;
    line-height: 1;
    letter-spacing: 1px;
    color: var(--text-main);
  }
  .tagline {
    position: absolute;
    left: 0;
    right: 0;
    top: 345px;
    text-align: center;
    font-size: 35px;
    font-weight: 700;
    color: var(--text-soft);
    letter-spacing: 0.3px;
  }
  .phone {
    position: absolute;
    left: 30px;
    bottom: 26px;
    font-size: 36px;
    font-weight: 600;
    letter-spacing: 1px;
  }
  .contact {
    position: absolute;
    right: 28px;
    bottom: 26px;
    text-align: right;
  }
  .website {
    font-size: 27px;
    font-weight: 600;
    color: var(--text-muted);
    margin-bottom: 10px;
  }
  .email {
    font-size: 36px;
    font-weight: 600;
    color: var(--text-main);
  }
</style>
</head>
<body>
  <main class="canvas">
    <section class="card-front">
      <h1 class="brand-name">Remy Vok</h1>
      <p class="tagline">magician - (public) speaker</p>
      <p class="phone">+32 471 265 903</p>
      <div class="contact">
        <p class="website">www.remy-vok.net</p>
        <p class="email">book@remy-vok.net</p>
      </div>
    </section>
  </main>
</body>
</html>
```